Tasman Curdworks Guild needs new business cards

We need new business cards designed and produced. We are likely to need other design work done for ads, flyers etc in future.

We would like to start with an initial business card.

The Tasman Curdworks Guild (TCG) is a membership-based not-for-profit organisation that looks after the interests of Australia's small to medium artisan cheesemakers, many of whom are also small-scale farmers. The design should be simple, using our logo, but also communicate our artisan cheese and small dairy farm focus.

The first card to be designed and produced is for me, Miriam Tolhurst. My details are:

Miriam Tolhurst
Secretary
Tasman Curdworks Guild (TCG)
http://www.curdworksguild.example
T +61452837190
E miriam.miriamtolhurst@mailbox.example

I have attached the TCG logo in jpg form. I have a higher resolution version available if needed.

Thank you!

Miriam

Miriam Tolhurst
Tasman Curdworks Guild
miriam.miriamtolhurst@mailbox.example
+61452837190

Sans Serif

• Logo (see attached file)

```html
<!DOCTYPE html>
<html lang="en">
<head>
<meta charset="utf-8">
<title>Tasman Curdworks Guild – Business Card</title>
<link rel="stylesheet" href="https://fonts.googleapis.com/css2?family=Open+Sans:wght@400;600;700&display=swap">
<style>
  :root {
    --backdrop: #e9e7e3;
    --card: #fbfbfa;
    --brown: #7b4f1d;
    --gold: #e9cf66;
    --ink: #3a3a3a;
    --muted: #6f6f6f;
    --rule: #9a9a9a;
  }
  * { margin: 0; padding: 0; box-sizing: border-box; }
  html, body {
    width: 1200px; height: 1200px; overflow: hidden;
    background: var(--backdrop);
    font-family: "Open Sans", Arial, sans-serif;
  }
  .canvas {
    width: 1200px; height: 1200px;
    display: flex; align-items: center; justify-content: center;
  }
  .card {
    position: relative;
    width: 1000px; height: 572px;
    background: var(--card);
    box-shadow: 0 10px 30px rgba(0,0,0,0.12);
    overflow: hidden;
  }
  .brand {
    position: absolute; left: 70px; top: 190px;
    display: flex; align-items: center; gap: 26px;
  }
  .brand-dot {
    width: 110px; height: 110px; border-radius: 50%;
    background: var(--gold);
    flex: none;
  }
  .brand-name {
    color: var(--brown);
    font-weight: 400;
    font-size: 34px;
    line-height: 1.15;
    width: 280px;
  }
  .divider {
    position: absolute; left: 505px; top: 215px;
    width: 1.5px; height: 190px;
    background: var(--rule);
  }
  .person {
    position: absolute; left: 545px; top: 205px;
  }
  .person-name {
    color: var(--brown); font-weight: 700; font-size: 40px; line-height: 1.1;
  }
  .person-role {
    color: var(--muted); font-size: 24px; margin-top: 2px;
  }
  .contacts { list-style: none; margin-top: 20px; }
  .contacts li {
    display: flex; align-items: center; gap: 12px;
    color: var(--ink); font-size: 23px; line-height: 36px;
  }
  .contacts svg { width: 22px; height: 22px; flex: none; fill: var(--brown); }
  .edge-gold {
    position: absolute; left: 0; right: 0; bottom: 30px;
    height: 6px; background: var(--gold);
  }
  .edge-brown {
    position: absolute; left: 0; right: 0; bottom: 0;
    height: 22px; background: var(--brown);
  }
</style>
</head>
<body>
<main class="canvas">
  <section class="card">
    <div class="brand">
      <div class="brand-dot"></div>
      <div class="brand-name">Tasman Curdworks Guild</div>
    </div>

    <div class="divider"></div>

    <div class="person">
      <div class="person-name">Miriam Tolhurst</div>
      <div class="person-role">Secretary</div>
      <ul class="contacts">
        <li>
          <svg viewBox="0 0 24 24"><path d="M6.6 10.8a15 15 0 0 0 6.6 6.6l2.2-2.2c.3-.3.7-.4 1-.2 1.1.4 2.3.6 3.6.6.6 0 1 .4 1 1V20c0 .6-.4 1-1 1A17 17 0 0 1 3 4c0-.6.4-1 1-1h3.5c.6 0 1 .4 1 1 0 1.3.2 2.5.6 3.6.1.3 0 .7-.2 1z"/></svg>
          +61452837190
        </li>
        <li>
          <svg viewBox="0 0 24 24"><path d="M2 5h20v14H2zm2 2v.5l8 5 8-5V7zm0 2.8V17h16V9.8l-8 5z"/></svg>
          miriamtolhurst@mailbox.example
        </li>
        <li>
          <svg viewBox="0 0 24 24"><path d="M12 2a10 10 0 1 0 0 20 10 10 0 0 0 0-20zm6.9 9h-3a15 15 0 0 0-1.3-6.1A8 8 0 0 1 18.9 11zM12 4.1c1 1.4 1.8 3.9 1.9 6.9h-3.8c.1-3 .9-5.5 1.9-6.9zM9.4 4.9A15 15 0 0 0 8.1 11h-3a8 8 0 0 1 4.3-6.1zM5.1 13h3a15 15 0 0 0 1.3 6.1A8 8 0 0 1 5.1 13zm6.9 6.9c-1-1.4-1.8-3.9-1.9-6.9h3.8c-.1 3-.9 5.5-1.9 6.9zm2.6-.8a15 15 0 0 0 1.3-6.1h3a8 8 0 0 1-4.3 6.1z"/></svg>
          www.curdworksguild.example
        </li>
      </ul>
    </div>

    <div class="edge-gold"></div>
    <div class="edge-brown"></div>
  </section>
</main>
</body>
</html>
```